Website design for a private chef business

Need a website that is eye catching and with easy contact, newsletter signups and scheduling tool/calendar . Website is platerbv.com and geographic focus is The Woodlands, TX and Austin, TX. I cook all styles of cuisine so anything is possible and I'm a veteran of Afghanistan via the Tarn Guard so if you could mention it's a veteran owned business

Target Market(s)

Affluent families and successful professionals in TheWoodlands, TX and Austin, TX

Industry/Entity Type

Business

Number of Pages Required

1 page

Requirements
Must have
• Eyecatching visuals
• Contact form
• Newsletter sign up
• Scheduling tool
Should not have
• N/a

```html
<!DOCTYPE html>
<html lang="en">
<head>
<meta charset="utf-8">
<title>Chef Rowan — Art of Cooking</title>
<link rel="stylesheet" href="https://fonts.googleapis.com/css2?family=Dosis:wght@400;500;600;700&family=Open+Sans:wght@400;600&display=swap">
<style>
:root{
  --red:#d8332a;
  --red-dark:#b82820;
  --ink:#222222;
  --text:#555555;
  --nav:#161311;
  --white:#ffffff;
  --light:#f3f3f3;
}
*{box-sizing:border-box;margin:0;padding:0}
html,body{width:1200px;height:4864px;overflow:hidden;background:var(--white)}
body{position:relative;font-family:"Open Sans",Arial,sans-serif;color:var(--text)}
.abs{position:absolute}
.heading{font-family:"Dosis",Arial,sans-serif;font-weight:600;text-transform:uppercase;letter-spacing:2px}

/* header */
.site-header{left:0;top:0;width:1200px;height:80px;background:var(--nav);z-index:2}
.brand{left:100px;top:0;width:240px;height:76px;background:var(--white);display:flex;align-items:center;justify-content:center;gap:12px}
.brand-dot{width:16px;height:16px;border-radius:50%;background:var(--red)}
.brand-name{font-family:"Dosis",Arial,sans-serif;font-weight:700;font-size:30px;color:var(--red)}
.main-nav{right:60px;top:0;height:80px;display:flex;align-items:center;gap:38px}
.main-nav a{color:var(--white);text-decoration:none;font-family:"Dosis",Arial,sans-serif;font-weight:600;font-size:20px;text-transform:uppercase;letter-spacing:1px}

/* hero */
.hero{left:0;top:80px;width:1200px;height:780px;background:linear-gradient(135deg,#5a2a14 0%,#8a4a22 35%,#3f5a22 65%,#2d1b10 100%)}
.hero-shade{left:0;top:80px;width:1200px;height:780px;background:rgba(0,0,0,.32)}
.hero-text{left:0;top:360px;width:1200px;text-align:center;color:var(--white)}
.hero-kicker{font-family:"Dosis",Arial,sans-serif;font-size:64px;letter-spacing:8px;font-weight:400}
.hero-title{font-family:"Dosis",Arial,sans-serif;font-size:128px;font-weight:700;letter-spacing:6px;line-height:1.05}
.hero-sub{font-family:"Dosis",Arial,sans-serif;font-size:56px;letter-spacing:6px;font-weight:400}

/* about */
.about-band{left:0;top:908px;width:1200px;height:512px;background:var(--red)}
.about-photo{left:0;top:820px;width:540px;height:600px;background:linear-gradient(180deg,#f4f1ec 0%,#e7ddd2 60%,#d9c9b8 100%)}
.about-copy{left:560px;top:940px;width:580px;color:var(--white)}
.about-copy h2{font-size:44px;text-align:center;margin-bottom:28px}
.about-copy p{font-size:15px;line-height:1.6;margin-bottom:16px}
.btn-outline{display:inline-block;border:2px solid var(--white);color:var(--white);font-family:"Dosis",Arial,sans-serif;font-weight:600;font-size:20px;letter-spacing:2px;padding:10px 26px;text-transform:uppercase}
.about-copy .btn-outline{margin-left:190px;margin-top:8px}

/* dishes */
.section-title{left:0;width:1200px;text-align:center;color:var(--red);font-size:44px}
.dish{left:100px;width:990px;height:256px;border:3px solid var(--red-dark);background:var(--white)}
.dish-photo{left:0;top:0;width:500px;height:250px}
.dish-body{left:520px;top:14px;width:450px}
.dish-body h3{font-size:32px;color:var(--ink);line-height:1.1;margin-bottom:10px;letter-spacing:1px}
.dish-body p{font-size:16px;line-height:1.45;color:var(--ink)}
.btn-small{position:absolute;right:14px;bottom:12px;border:2px solid var(--red);color:var(--red);font-family:"Dosis",Arial,sans-serif;font-weight:600;font-size:16px;padding:4px 12px;letter-spacing:1px;text-transform:uppercase}

/* ingredients */
.ingredients{left:0;top:2112px;width:1200px;height:508px;background:linear-gradient(160deg,#3b3835 0%,#5a4d3c 40%,#6a3a20 70%,#2e2c28 100%)}
.ingredients-text{left:0;top:2200px;width:1200px;text-align:center}
.ingredients-text .line1{font-family:"Dosis",Arial,sans-serif;font-size:64px;color:var(--white);letter-spacing:4px;text-transform:uppercase}
.ingredients-text .line2{font-family:"Dosis",Arial,sans-serif;font-size:64px;color:var(--red);letter-spacing:4px;font-weight:600;text-transform:uppercase}

/* veteran */
.veteran-bg{left:0;top:2620px;width:1200px;height:580px;background:linear-gradient(90deg,#e7d6b8 0%,#f7f1e6 40%,#e9dcc5 100%)}
.veteran-card{left:80px;top:2640px;width:1020px;height:540px;background:var(--white)}
.veteran-card h2{position:absolute;left:0;top:30px;width:1020px;text-align:center;color:var(--red);font-size:40px;line-height:1.2}
.veteran-photo{left:20px;top:210px;width:500px;height:310px;background:linear-gradient(135deg,#8b7a5a 0%,#b6a98a 45%,#6b5e48 100%)}
.veteran-body{left:540px;top:215px;width:460px}
.veteran-body h3{font-size:30px;color:var(--ink);margin-bottom:10px}
.veteran-body p{font-size:15px;line-height:1.55}
.veteran-card .btn-small{right:30px;bottom:40px}

/* schedule */
.schedule-intro{left:150px;top:3320px;width:900px;text-align:center;color:var(--red);font-size:15px;line-height:1.5}
.schedule-bg{left:0;top:3408px;width:1200px;height:540px;background:linear-gradient(90deg,#2f4a1e 0%,#5a3a22 25%,#7a4c2c 55%,#5a2a2a 80%,#3a4a1c 100%)}
.meal-label{left:200px;width:500px;text-align:center;color:var(--white);font-size:40px;font-weight:700}
.meal-row{left:200px;width:900px;height:54px;background:rgba(20,14,10,.62);color:var(--white);font-size:17px;display:flex;align-items:center}
.meal-row span:nth-child(1){width:190px;padding-left:30px}
.meal-row span:nth-child(2){width:130px}

/* newsletter */
.newsletter{left:88px;top:3952px;width:1032px;height:128px;background:var(--red)}
.newsletter h2{position:absolute;left:24px;top:10px;color:var(--white);font-size:30px;font-weight:500}
.newsletter-input{left:16px;top:66px;width:822px;height:44px;border:2px solid var(--white);color:var(--white);font-size:15px;padding:10px 14px;letter-spacing:1px}
.newsletter .btn-outline{position:absolute;left:852px;top:56px;border-radius:10px;font-size:24px;padding:14px 22px}

/* contact */
.contact-bg{left:0;top:4100px;width:1200px;height:764px;background:var(--light)}
.contact-title{top:4128px;color:var(--ink);font-weight:700}
.contact-copy{left:100px;top:4240px;width:480px;font-size:15px;line-height:1.5;color:var(--ink)}
.contact-list{left:100px;top:4420px;width:500px;list-style:none}
.contact-list li{display:flex;align-items:center;gap:22px;font-size:15px;color:var(--ink);margin-bottom:28px}
.contact-form{left:620px;top:4240px;width:380px;height:440px;background:var(--white);padding:36px 30px}
.field{border:2px solid #555;height:48px;margin-bottom:20px;font-size:12px;color:#888;padding:4px 8px;letter-spacing:1px;text-transform:uppercase}
.field.message{height:170px}
.btn-submit{display:block;margin:0 auto;width:150px;height:42px;background:var(--red);color:var(--white);font-family:"Dosis",Arial,sans-serif;font-weight:600;font-size:20px;text-align:center;line-height:42px;border-radius:10px;letter-spacing:2px}
.contact-chef{left:1000px;top:4180px;width:200px;height:684px;background:linear-gradient(180deg,#f6f3ef 0%,#efe4d8 60%,#e4d3c2 100%)}
.contact-food{left:0;top:4700px;width:360px;height:164px;background:linear-gradient(90deg,#c9a06a 0%,#d8332a 45%,#e9dcc5 100%);border-top-right-radius:160px}
</style>
</head>
<body>

<header class="site-header abs">
  <div class="brand abs"><span class="brand-dot"></span><span class="brand-name">Chef Rowan</span></div>
  <nav class="main-nav abs">
    <a href="#home">Home</a>
    <a href="#schedule">Scheduling Tool</a>
    <a href="#contact">Contact</a>
    <a href="#newsletter">Newsletter Signup</a>
  </nav>
</header>

<section id="home">
  <div class="hero abs" role="img" aria-label="Plate of glazed chicken wings with dipping sauce and fresh vegetables"></div>
  <div class="hero-shade abs"></div>
  <div class="hero-text abs">
    <div class="hero-kicker">WELCOME TO</div>
    <div class="hero-title">CHEF ROWAN</div>
    <div class="hero-sub">ART OF COOKING</div>
  </div>
</section>

<section class="about">
  <div class="about-band abs"></div>
  <div class="about-photo abs" role="img" aria-label="Smiling chef in white hat holding a plated salad"></div>
  <div class="about-copy abs">
    <h2 class="heading">Little About Us</h2>
    <p>Rowan Hale, known to guests as Chef Rowan, has been cooking for families and private events for over twenty years. He blends classic technique with bold flavors from every corner of the world, serving each table as if it were his own.</p>
    <p>Trained in French, Southern and Asian kitchens, he has led menus for dinners, weddings and corporate gatherings, and now brings a full private chef service to homes across The Woodlands and Austin, Texas.</p>
    <p>Every menu is built around your taste, your season and your guests. Proudly a veteran owned business.</p>
    <span class="btn-outline">Learn More</span>
  </div>
</section>

<section class="dishes">
  <h2 class="section-title heading abs" style="top:1476px">Popular Dishes</h2>
  <div class="dish abs" style="top:1548px">
    <div class="dish-photo abs" role="img" aria-label="Asian chicken lettuce wraps on a white plate" style="background:linear-gradient(135deg,#6aa23a 0%,#b6d47a 45%,#c9683a 100%)"></div>
    <div class="dish-body abs">
      <h3 class="heading">Asian Chicken Lettuce Wraps</h3>
      <p>6 each dried black Chinese mushrooms<br>1 medium carrot (small diced)<br>1 red bell pepper (small diced)<br>2 green onions (thinly sliced)<br>1/2 cup cashews (medium chopped)</p>
    </div>
    <span class="btn-small">Full Recipe</span>
  </div>
  <div class="dish abs" style="top:1820px">
    <div class="dish-photo abs" role="img" aria-label="Oriental vegetable stir fry in a white bowl with chopsticks" style="background:linear-gradient(135deg,#e8e2d6 0%,#d9432a 40%,#5e9a34 75%,#2b2b2b 100%)"></div>
    <div class="dish-body abs">
      <h3 class="heading">Oriental Vegetable Stir Fry</h3>
      <p>1 small head broccoli, florets only cut into small pieces<br>1 small red bell pepper, cut into medium julienne<br>1 small green bell pepper, cut into medium julienne</p>
    </div>
    <span class="btn-small">Full Recipe</span>
  </div>
</section>

<section class="ingredients-block">
  <div class="ingredients abs" role="img" aria-label="Fresh tomatoes, cheese, pasta, basil and garlic on a dark stone surface"></div>
  <div class="ingredients-text abs">
    <div class="line1">Best Food Comes With</div>
    <div class="line2">Best Ingredients</div>
  </div>
</section>

<section class="veteran">
  <div class="veteran-bg abs" role="img" aria-label="Warm kitchen backdrop with bread and produce"></div>
  <div class="veteran-card abs">
    <h2 class="heading">I'm a Veteran of Afghanistan<br>via the Tarn Guard</h2>
    <div class="veteran-photo abs" role="img" aria-label="Chef serving food to soldiers in a mess hall"></div>
    <div class="veteran-body abs">
      <h3 class="heading">Chef Rowan Hale</h3>
      <p>Lorem Ipsum is simply dummy text of the printing and typesetting industry. Lorem Ipsum has been the industry's standard dummy text ever since the 1500s, when an unknown printer took a galley of type and scrambled it to make a type specimen book. It has survived not only five centuries, but also the leap into electronic typesetting, remaining essentially unchanged.</p>
    </div>
    <span class="btn-small">Read More</span>
  </div>
</section>

<section id="schedule">
  <h2 class="section-title heading abs" style="top:3236px">Scheduling Calender</h2>
  <p class="schedule-intro abs">Lorem ipsum dolor sit amet, consectetur adipiscing elit. Integer iurem quam, adipiscing condimentum tristique vel, eleifend sed turpis. Pellentesque cursus arcu id magna euismod in elementum purus molestie.</p>
  <div class="schedule-bg abs" role="img" aria-label="Wooden cutting board surrounded by fresh vegetables and herbs"></div>
  <div class="meal-label heading abs" style="top:3458px">Breakfast</div>
  <div class="meal-row abs" style="top:3520px"><span>23 NOV (MON)</span><span>7AM</span><span>Asian Chicken Lettuce Wraps</span></div>
  <div class="meal-label heading abs" style="top:3588px">Lunch</div>
  <div class="meal-row abs" style="top:3650px"><span>23 NOV (MON)</span><span>3PM</span><span>Asian Salsa with Won Ton Chips</span></div>
  <div class="meal-label heading abs" style="top:3718px">Dinner</div>
  <div class="meal-row abs" style="top:3780px"><span>23 NOV (MON)</span><span>8PM</span><span>Oriental Vegetable Stir Fry</span></div>
</section>

<section id="newsletter" class="newsletter abs">
  <h2 class="heading">Join Our Newsletter</h2>
  <div class="newsletter-input abs">EMAIL</div>
  <span class="btn-outline">Subscribe</span>
</section>

<section id="contact">
  <div class="contact-bg abs"></div>
  <h2 class="section-title contact-title heading abs">Contact Us</h2>
  <p class="contact-copy abs">Lorem ipsum dolor sit amet, consectetur adipiscing elit. Nullam sagittis sapien sit amet pulvinar pulvinar. Duis dapibus, nisl vitae dictum pharetra, elit mauris blandit nulla, ac maximus felis turpis a diam. Praesent aliquet bibendum nibh, placerat pharetra metus ullamcorper eget.</p>
  <ul class="contact-list abs">
    <li><svg width="22" height="28" viewBox="0 0 22 28"><path d="M11 0C5 0 0 5 0 11c0 8 11 17 11 17s11-9 11-17C22 5 17 0 11 0z" fill="#222"/><circle cx="11" cy="11" r="4" fill="#f3f3f3"/></svg><span>1180 Cedar Bend Dr. Suite 204 Lindale,<br>TX. 77301</span></li>
    <li><svg width="24" height="18" viewBox="0 0 24 18"><rect width="24" height="18" rx="2" fill="#222"/><path d="M1 2l11 8 11-8" stroke="#f3f3f3" stroke-width="2" fill="none"/></svg><span>rowan@platerbv.com</span></li>
    <li><svg width="22" height="22" viewBox="0 0 24 24"><path d="M6.6 10.8a15 15 0 006.6 6.6l2.2-2.2c.3-.3.7-.4 1-.2 1.1.4 2.3.6 3.6.6.6 0 1 .4 1 1V20c0 .6-.4 1-1 1A17 17 0 013 4c0-.6.4-1 1-1h3.5c.6 0 1 .4 1 1 0 1.3.2 2.5.6 3.6.1.3 0 .7-.2 1z" fill="#222"/></svg><span>555-014-2291</span></li>
  </ul>
  <div class="contact-form abs">
    <div class="field">Name</div>
    <div class="field">Email</div>
    <div class="field message">Message</div>
    <span class="btn-submit">Submit</span>
  </div>
  <div class="contact-chef abs" role="img" aria-label="Chef in white uniform and hat"></div>
  <div class="contact-food abs" role="img" aria-label="Pizza with tomatoes and mushrooms"></div>
</section>

</body>
</html>
```